Clean and modern business cards

Looking for an updated business card design for my dental office “corvanta dental” . Looking for a modern clean / sleek design . I’m thinking black background but open to seeing other options . One side needs to have an appointment card . Card needs to have logo, dentist name , phone, email , address . I’ve attached couple of cards I thought were cool as well as my logo
Target Market(s)
Dental patients
Industry/Entity Type
Dentistry
Contact Information for Business Card
Phone email address

```html
<!DOCTYPE html>
<html lang="en">
<head>
<meta charset="utf-8">
<title>Corvanta Dental – Business Cards</title>
<link href="https://fonts.googleapis.com/css2?family=Quicksand:wght@500;600;700&display=swap" rel="stylesheet">
<style>
  :root{
    --bg:#e9e6e1;
    --card-white:#ffffff;
    --card-black:#050606;
    --ink:#3a3a3a;
    --green:#8ab43c;
    --orange:#e8512d;
    --yellow:#f2b824;
    --purple:#7b4ea3;
    --blue:#3fa3c9;
    --white:#ffffff;
  }
  *{margin:0;padding:0;box-sizing:border-box}
  html,body{width:1200px;height:900px;overflow:hidden}
  body{background:var(--bg);font-family:"Quicksand",sans-serif;color:var(--ink);position:relative}
  .card{position:absolute;left:285px;width:630px;height:360px;border-radius:22px;overflow:hidden;box-shadow:0 6px 18px rgba(0,0,0,.15)}
  .card--front{top:50px;background:var(--card-white)}
  .card--back{top:490px;background:var(--card-black)}

  .decor{position:absolute;right:0;top:0;width:300px;height:100%}
  .card--front .decor{background:radial-gradient(circle at 60% 55%,rgba(123,78,163,.14),rgba(63,163,201,.10) 40%,rgba(242,184,36,.08) 60%,rgba(255,255,255,0) 78%)}
  .card--back .decor{background:radial-gradient(circle at 60% 50%,rgba(123,78,163,.22),rgba(63,163,201,.14) 40%,rgba(138,180,60,.10) 60%,rgba(5,6,6,0) 80%)}

  .brand{position:absolute;display:flex;align-items:center;gap:14px;white-space:nowrap}
  .brand__dot{width:44px;height:44px;border-radius:50%;background:var(--blue);flex:none}
  .brand__name{font-weight:700;font-size:28px;letter-spacing:.5px;line-height:1;text-transform:uppercase}
  .card--front .brand{left:270px;top:30px}
  .card--front .brand__name{color:#111}

  .contact{position:absolute;left:34px;top:86px;list-style:none;font-size:14px;font-weight:500;line-height:1.3}
  .contact li{display:flex;align-items:flex-start;gap:10px;margin-bottom:3px}
  .contact svg{flex:none;width:15px;height:15px;margin-top:2px}

  .appointment{position:absolute;left:34px;top:206px;width:440px}
  .appointment__title{color:var(--green);font-size:17px;font-weight:600;line-height:1.2;margin-bottom:6px}
  .appointment__field{display:flex;align-items:flex-end;gap:8px;color:var(--green);font-size:14px;font-weight:500;line-height:1.2;margin-bottom:6px;width:380px}
  .appointment__line{flex:1;border-bottom:1.5px dashed var(--green);height:12px}
  .appointment__note{margin-top:8px;color:var(--orange);font-size:14px;font-weight:600;line-height:1.3;width:430px}

  .card--back .brand{left:150px;top:140px}
  .card--back .brand__name{color:var(--white);font-size:36px}
  .dentist{position:absolute;left:210px;top:96px;color:var(--orange);font-size:18px;font-weight:600;letter-spacing:.5px;text-transform:uppercase;white-space:nowrap}
  .dentist-rule{position:absolute;left:210px;top:126px;width:250px;height:2px;background:var(--green)}
</style>
</head>
<body>

<section class="card card--front">
  <div class="decor" role="img" aria-label="Soft multicoloured bubble pattern with a faint large tooth decoration"></div>

  <div class="brand">
    <span class="brand__dot"></span>
    <span class="brand__name">Corvanta Dental</span>
  </div>

  <ul class="contact">
    <li>
      <svg viewBox="0 0 16 16"><path fill="var(--yellow)" d="M3 2h3l1 3-2 1c1 2 2 3 4 4l1-2 3 1v3c0 1-1 2-2 2C6 14 2 10 2 4c0-1 0-2 1-2z"/></svg>
      (204) 555 - 0187
    </li>
    <li>
      <svg viewBox="0 0 16 16"><circle cx="8" cy="8" r="7" fill="var(--green)"/><path d="M1 8h14M8 1c3 3 3 11 0 14M8 1c-3 3-3 11 0 14" stroke="#fff" stroke-width="1" fill="none"/></svg>
      corvantadental.ca
    </li>
    <li>
      <svg viewBox="0 0 16 16"><rect x="1" y="4" width="14" height="9" rx="1.5" fill="var(--purple)"/><path d="M1.5 4.5 8 9.5l6.5-5" stroke="#fff" stroke-width="1.2" fill="none"/></svg>
      hello@corvantadental.ca
    </li>
    <li>
      <svg viewBox="0 0 16 16"><path fill="var(--orange)" d="M8 1a5 5 0 0 1 5 5c0 4-5 9-5 9S3 10 3 6a5 5 0 0 1 5-5z"/><circle cx="8" cy="6" r="2" fill="#fff"/></svg>
      <span>210 – 4480 Riverbend Ave<br>Winnipeg, MB R2K 3L8</span>
    </li>
  </ul>

  <div class="appointment">
    <p class="appointment__title">Your Next Appointment is</p>
    <div class="appointment__field">Date <span class="appointment__line"></span></div>
    <div class="appointment__field">Time <span class="appointment__line"></span></div>
    <p class="appointment__note">To cancel or reschedule please notify us at least 48 hours prior to your scheduled appointment.</p>
  </div>
</section>

<section class="card card--back">
  <div class="decor" role="img" aria-label="Dim multicoloured bubble pattern with a faint large tooth decoration"></div>
  <p class="dentist">Dr. Elias Marten</p>
  <span class="dentist-rule"></span>
  <div class="brand">
    <span class="brand__dot"></span>
    <span class="brand__name">Corvanta Dental</span>
  </div>
</section>

</body>
</html>
```